Pitch book for the 2025 K7R Global Skycup event in Muncie, Indiana, USA

Title: Fueling the Future of Aeromodeling: Sponsor the 2025 K7R Global Skycup
1. Event Overview
What: The 2025 ORV K7R Global Skycup for Aerobatic Model Aircraft.
When: August 9–16, 2025.
Where: Institute for Scale Flightcraft (ISF) Headquarters, Muncie, Indiana.
Hosted by: Institute for Scale Flightcraft (ISF) in partnership with the Federated Guild for Remote Stunt Piloting (FGRSP).
Participants: Top pilots from across the globe, including juniors and female competitors.
2. Why Sponsor?
Shaping the Future Workforce: Inspire youth to explore careers in aerospace, aviation, and unmanned systems (drones, RPVs), bridging hobbies and high-tech industries like Corvane, Halbrook Teller, and more.
Brand Visibility: Engage with a global audience of enthusiasts, professionals, and media at a premier international event.
Community Impact: Support an event that promotes innovation, STEM education, and cultural exchange.
3. Key Features of the Event
Cutting-Edge Venue: Over 1,100 acres of flying space tailored for precision aerobatics.
Diverse Competitions: Featuring junior and female classifications alongside world-class competitors.
Global Audience: Media coverage, live streams, and on-site spectators.
4. Sponsorship Opportunities
Title Sponsor ($50,000):
Naming rights: "Your Brand Presents the 2025 K7R Global Skycup."
Logo placement on all event materials, website, and livestreams.
Prime exhibit space at the venue.
Gold Sponsor ($25,000):
Prominent branding on materials and media.
Speaking opportunity at the opening or closing ceremony.
Silver Sponsor ($10,000):
Recognition in event communications.
Inclusion in the sponsor wall at the venue.
Event Sponsor ($5,000):
Branding on specific activities (e.g., banquet, practice days).
Custom Sponsorships: Tailored to fit corporate goals, including STEM outreach and branded giveaways.
5. Audience Demographics
Competitors: Over 100 elite pilots from 40+ countries.
Spectators & Supporters: Thousands of attendees, ranging from hobbyists to industry professionals.
Media Reach: Coverage by international aeromodelling and aerospace outlets.
6. STEM and Industry Connections
Showcase pathways from aeromodelling to careers in aviation, engineering, and defense.
Collaborate with sponsors on outreach programs for local schools and universities.
7. Marketing Benefits
Digital: Inclusion in newsletters, website, and social media campaigns.
On-Site Branding: Banners, booths, and branded giveaways.
Networking: Access to high-value attendees and industry leaders.
8. Budget Breakdown
Goal: Raise $180,000 to support the championship.
Funding Allocation:
$70,000: Event logistics (venue, staff, equipment).
$50,000: Participant support (travel subsidies, junior competitor outreach).
$30,000: Marketing and media coverage.
$20,000: Amenities and hospitality.
9. Call to Action
Be Part of the Legacy: Join us in creating a memorable event that not only crowns world champions but also inspires future innovators.
Contact Information:
Name: [Your Name]
Email: [Your Email]
Phone: [Your Phone]
Website: [Event Website Link]

```html
<!DOCTYPE html>
<html lang="en">
<head>
<meta charset="utf-8">
<title>Sponsor the 2025 K7R Global Skycup</title>
<link href="https://fonts.googleapis.com/css2?family=Roboto+Condensed:wght@300;400;500;700&display=swap" rel="stylesheet">
<style>
  :root{
    --maroon:#7d1d3a;
    --maroon-deep:#6a1630;
    --maroon-soft:#8d2a48;
    --ink:#1d1d1f;
    --white:#ffffff;
    --page-bg:#ffffff;
  }
  *{box-sizing:border-box;margin:0;padding:0}
  html,body{width:1200px;height:2194px;overflow:hidden;background:var(--page-bg)}
  body{font-family:"Roboto Condensed",sans-serif;color:var(--ink);position:relative}
  .page{position:absolute;left:244px;width:712px;height:1008px;overflow:hidden;background:var(--white)}
  .page--cover{top:62px}
  .page--details{top:1122px}

  /* Cover page */
  .cover-hero{position:absolute;left:0;top:0;width:406px;height:545px;
    background:linear-gradient(160deg,#8a2a45 0%,var(--maroon) 55%,#6e1a33 100%)}
  .cover-photo{position:absolute;left:406px;top:0;width:306px;height:545px;
    background:linear-gradient(180deg,#c9d6e2 0%,#b7c4cf 30%,#c7a7b5 50%,#9c8a6d 75%,#7b6a4e 100%)}
  .cover-title{position:absolute;left:38px;top:52px;width:360px;color:var(--white);
    font-weight:700;font-size:40px;line-height:51px}
  .cover-sub{position:absolute;left:38px;top:346px;width:330px;color:var(--white);
    font-weight:500;font-size:23px;line-height:28px}
  .cover-date{position:absolute;left:38px;top:470px;color:var(--white);font-weight:700;font-size:40px}
  .cover-info{position:absolute;left:0;top:545px;width:406px;height:463px;background:var(--maroon);color:var(--white)}
  .info-label{position:absolute;left:38px;top:68px;font-size:23px;font-weight:500}
  .info-text{position:absolute;left:38px;top:98px;width:360px;font-size:22px;font-weight:300;line-height:28px}
  .info-host{position:absolute;left:38px;top:224px;width:320px;font-size:17px;font-weight:300;line-height:23px}
  .info-host em{font-style:italic;font-weight:700}
  .info-participants{position:absolute;left:38px;top:362px;width:340px;font-size:15px;font-weight:700;line-height:20px}
  .cover-side{position:absolute;left:406px;top:545px;width:306px;height:463px;padding:40px 30px 0 32px}
  .side-heading{font-size:24px;font-weight:500;line-height:29px;color:var(--ink)}
  .side-text{font-size:10.5px;line-height:14px;font-weight:300;margin-top:12px}
  .side-text b{font-weight:700}
  .side-text + .side-heading{margin-top:26px}

  /* Details page */
  .team-photo{position:absolute;left:0;top:0;width:712px;height:369px;
    background:linear-gradient(180deg,#b9cde0 0%,#d7e2ea 35%,#e8e8e6 55%,#a99a78 100%)}
  .detail-left{position:absolute;left:0;top:369px;width:332px;height:639px;
    background:linear-gradient(180deg,#ffffff 0%,#ffffff 50%,#c9ccd0 66%,#6d6b63 82%,#1d1c1a 100%)}
  .field-photo{position:absolute;left:0;top:330px;width:332px;height:309px}
  .detail-right{position:absolute;left:332px;top:369px;width:380px;height:639px;
    background:linear-gradient(180deg,var(--maroon) 0%,var(--maroon) 45%,var(--maroon-soft) 70%,var(--maroon-deep) 100%);color:var(--white)}
  .opps{position:absolute;left:38px;top:22px;width:285px}
  .opps-heading{font-size:24px;font-weight:500;margin-bottom:14px}
  .tier{margin-bottom:12px}
  .tier-name{font-size:15px;font-weight:500}
  .tier-text{font-size:10px;line-height:13.5px;font-weight:300}
  .cta{position:absolute;left:38px;top:510px;width:250px;color:var(--white)}
  .cta-heading{font-size:24px;font-weight:500}
  .cta-text{font-size:10px;line-height:13.5px;font-weight:300}
  .right-block{position:absolute;left:22px;width:340px}
  .right-heading{font-size:24px;font-weight:700;line-height:30px}
  .right-text{font-size:10px;line-height:14px;font-weight:300;margin-top:2px}
  .contact{position:absolute;right:38px;top:515px;text-align:right}
  .contact-heading{font-size:24px;font-weight:700}
  .contact-line{font-size:15px;font-weight:300;line-height:20px}
</style>
</head>
<body>

<section class="page page--cover">
  <div class="cover-photo" role="img" aria-label="Close-up photo of a pink and white aerobatic model aircraft with a black propeller on a grass field"></div>
  <div class="cover-hero" role="img" aria-label="Maroon-tinted photo of the aircraft propeller and nose"></div>
  <h1 class="cover-title">Fueling the Future of Aeromodeling: Sponsor the 2025 K7R Global Skycup</h1>
  <p class="cover-sub">The 2025 ORV K7R Global Skycup for Aerobatic Model Aircraft.</p>
  <p class="cover-date">August 9–16, 2025</p>

  <div class="cover-info">
    <p class="info-label">Location:</p>
    <p class="info-text">Institute for Scale Flightcraft (ISF) Headquarters, Muncie, Indiana.</p>
    <p class="info-host"><em>Hosted by:</em> Institute for Scale Flightcraft (ISF) in partnership with the Federated Guild for Remote Stunt Piloting (FGRSP).</p>
    <p class="info-participants">Participants: Top pilots from across the globe, including juniors and female competitors.</p>
  </div>

  <div class="cover-side">
    <h2 class="side-heading">Why Sponsor?</h2>
    <p class="side-text"><b>Shaping the Future Workforce:</b> Inspire youth to explore careers in aerospace, aviation, and unmanned systems (drones, RPVs), bridging hobbies and high-tech industries like Corvane, Halbrook Teller, and more.<br>
    <b>Brand Visibility:</b> Engage with a global audience of enthusiasts, professionals, and media at a premier international event.<br>
    Community Impact: Support an event that promotes innovation, STEM education, and cultural exchange.</p>
    <h2 class="side-heading">Key Features of the Event</h2>
    <p class="side-text"><b>Cutting-Edge Venue:</b> Over 1,100 acres of flying space tailored for precision aerobatics.<br>
    <b>Diverse Competitions:</b> Featuring junior and female classifications alongside world-class competitors.<br>
    <b>Global Audience:</b> Media coverage, live streams, and on-site spectators.</p>
  </div>
</section>

<section class="page page--details">
  <div class="team-photo" role="img" aria-label="Team photo of pilots in white polo shirts holding a colorful aerobatic model aircraft at the flying field"></div>

  <div class="detail-left">
    <div class="field-photo" role="img" aria-label="Photo of pilots preparing model aircraft on the flight line"></div>
    <div class="opps">
      <h2 class="opps-heading">Sponsorship Opportunities</h2>
      <div class="tier">
        <p class="tier-name">Title Sponsor ($50,000):</p>
        <p class="tier-text">Naming rights: "Your Brand Presents the 2025 K7R Global Skycup."<br>Logo placement on all event materials, website, and livestreams.<br>Prime exhibit space at the venue.</p>
      </div>
      <div class="tier">
        <p class="tier-name">Gold Sponsor ($25,000):</p>
        <p class="tier-text">Prominent branding on materials and media.<br>Speaking opportunity at the opening or closing ceremony.</p>
      </div>
      <div class="tier">
        <p class="tier-name">Silver Sponsor ($10,000):</p>
        <p class="tier-text">Recognition in event communications.<br>Inclusion in the sponsor wall at the venue.</p>
      </div>
      <div class="tier">
        <p class="tier-name">Event Sponsor ($5,000):</p>
        <p class="tier-text">Branding on specific activities (e.g., banquet, practice days).<br>Custom Sponsorships: Tailored to fit corporate goals, including STEM outreach and branded giveaways.</p>
      </div>
    </div>
    <div class="cta">
      <h2 class="cta-heading">Call to Action</h2>
      <p class="cta-text">Be Part of the Legacy: Join us in creating a memorable event that not only crowns world champions but also inspires future innovators.</p>
    </div>
  </div>

  <div class="detail-right">
    <div class="right-block" style="top:14px">
      <h2 class="right-heading">Audience Demographics</h2>
      <p class="right-text">Competitors: Over 100 elite pilots from 40+ countries.<br>Spectators &amp; Supporters: Thousands of attendees, ranging from hobbyists to industry professionals.<br>Media Reach: Coverage by international aeromodelling and aerospace outlets.</p>
    </div>
    <div class="right-block" style="top:136px">
      <h2 class="right-heading">STEM and Industry Connections</h2>
      <p class="right-text">Showcase pathways from aeromodelling to careers in aviation, engineering, and defense.<br>Collaborate with sponsors on outreach programs for local schools and universities.</p>
    </div>
    <div class="right-block" style="top:269px">
      <h2 class="right-heading">Marketing Benefits</h2>
      <p class="right-text">Digital: Inclusion in newsletters, website, and social media campaigns.<br>On-Site Branding: Banners, booths, and branded giveaways.<br>Networking: Access to high-value attendees and industry leaders.</p>
    </div>
    <div class="right-block" style="top:362px">
      <h2 class="right-heading">Budget Breakdown</h2>
      <p class="right-text">Goal: Raise $180,000 to support the championship.<br>Funding Allocation:<br>$70,000: Event logistics (venue, staff, equipment).<br>$50,000: Participant support (travel subsidies, junior competitor outreach).<br>$30,000: Marketing and media coverage.<br>$20,000: Amenities and hospitality.</p>
    </div>
    <div class="contact">
      <h2 class="contact-heading">Contact Information:</h2>
      <p class="contact-line">555 014 2876</p>
      <p class="contact-line">info@k7rskycup.org</p>
      <p class="contact-line">www.k7rskycup.org</p>
    </div>
  </div>
</section>

</body>
</html>
```